Business card for Bio pharmaceutical company

Hello,
We are a bio pharmaceutical contract manufacturing company in Brisbane, Australia. Can you please create a new business card design. Please go to our website for colours http://www.veltromedix.com.au.
On the back can you include the cartoon mascot Tobi Warn and the tagline
"A Global Biopharmaceutical Contract Development Manufacturing Company"
Target Market(s)
Biotechnology
Industry/Entity Type
Pharmaceutical
Contact Information for Business Card
Karen Holbrooke
Business Development Manager
karen.holbrooke@veltromedix.com.au
1937 Mulgrave Street Kelby Queesnland 4076 Australia
T: +61 7 3591 6042
M +61 427 516 908
F +61 7 3648 2095
www.veltromedix.com.au

```html
<!DOCTYPE html>
<html lang="en">
<head>
<meta charset="utf-8">
<title>VeltroMedix Business Card</title>
<link rel="stylesheet" href="https://fonts.googleapis.com/css2?family=Arimo:wght@400;700&display=swap">
<style>
  :root {
    --bg: #ececec;
    --card-top: #2fbfa6;
    --card-mid: #3bb6c0;
    --card-bottom: #2b9cc9;
    --back-top: #4fc4b6;
    --back-bottom: #3aa2cc;
    --ink: #1d2a33;
    --brand: #173e6e;
    --mascot-a: #74c7e6;
    --mascot-b: #3f97c7;
  }
  * { margin: 0; padding: 0; box-sizing: border-box; }
  html, body {
    width: 1200px; height: 900px; overflow: hidden;
    background: var(--bg);
    font-family: "Arimo", Arial, sans-serif;
    color: var(--ink);
  }
  .canvas { position: relative; width: 1200px; height: 900px; }
  .card {
    position: absolute; left: 250px; width: 700px; height: 400px;
    box-shadow: 0 6px 18px rgba(0,0,0,0.12);
  }
  .card-back {
    top: 30px;
    background: linear-gradient(160deg, var(--back-top) 0%, var(--back-bottom) 100%);
  }
  .mascot {
    position: absolute; left: 260px; top: 70px; width: 180px; height: 200px;
    border-radius: 90px;
    background: radial-gradient(circle at 45% 40%, var(--mascot-a), var(--mascot-b));
    opacity: 0.9;
  }
  .tagline {
    position: absolute; left: 0; right: 0; top: 318px;
    text-align: center; font-size: 14px; font-weight: 700;
  }
  .card-front {
    top: 470px;
    background: linear-gradient(180deg, var(--card-top) 0%, var(--card-mid) 55%, var(--card-bottom) 100%);
  }
  .brand {
    position: absolute; left: 44px; top: 60px;
    display: flex; align-items: center; gap: 10px;
  }
  .brand-name { font-size: 34px; font-weight: 700; color: var(--brand); letter-spacing: -0.5px; }
  .brand-mark { width: 14px; height: 14px; background: var(--brand); }
  .web-links {
    position: absolute; right: 36px; top: 40px; text-align: right;
    font-size: 15px; font-weight: 700; line-height: 1.55;
  }
  .web-links .email { font-weight: 400; font-size: 14px; }
  .person { position: absolute; left: 44px; top: 160px; }
  .person-name { font-size: 25px; font-weight: 700; line-height: 1.1; }
  .person-role { font-size: 16px; font-weight: 700; }
  .address {
    position: absolute; left: 44px; top: 330px;
    font-size: 17px; font-weight: 700;
  }
  .contact {
    position: absolute; right: 50px; top: 248px; text-align: right;
    font-size: 16px; font-weight: 700; line-height: 1.45;
  }
</style>
</head>
<body>
<main class="canvas">
  <section class="card card-back" aria-label="Card back">
    <div class="mascot" role="img" aria-label="Cartoon mascot Tobi Warn, a friendly blue bacterium character"></div>
    <p class="tagline">A Global Biopharmaceutical Contract Development Manufacturing Company</p>
  </section>

  <section class="card card-front" aria-label="Card front">
    <div class="brand">
      <span class="brand-name">VeltroMedix</span>
      <span class="brand-mark"></span>
    </div>
    <div class="web-links">
      <p>www.veltromedix.com.au</p>
      <p class="email">karen.holbrooke@veltromedix.com.au</p>
    </div>
    <div class="person">
      <p class="person-name">Karen Holbrooke</p>
      <p class="person-role">Business Development Manager</p>
    </div>
    <p class="address">1937 Mulgrave Street Kelby Queesnland 4189</p>
    <div class="contact">
      <p>Australia</p>
      <p>T: +61 7 3591 6042</p>
      <p>M +61 427 516 908</p>
      <p>F +61 7 3648 2095</p>
    </div>
  </section>
</main>
</body>
</html>
```